Veterinary Clinic Letterhead - Ridgeview Veterinary Surgery

We need a letterhead design for an established Veterinary Clinic in Ashcombe called Ridgeview Veterinary Surgery. We are a moderate sized mixed animal veterinary clinic offering a wide variety of veterinary services. The design should use the same colour pattern as those in the logos supplied. The design should also include our address (48 Tulloch Road, Ashcombe, Tablelands, 4890), phone number (07 4158 6734), email (admin@ridgeviewvets.com.au), website (www.ridgeviewvets.com.au) and our opening hours (7am to 6pm Monday to Friday and 9am to 1pm Saturday).
Target Market(s)
Pet owners
Industry/Entity Type
Veterinary
Requirements
Must have
- The logo or modification of it, business address, opening hours, website, phone number and email address

```html
<!DOCTYPE html>
<html lang="en">
<head>
<meta charset="utf-8">
<title>Ridgeview Veterinary Surgery – Letterhead</title>
<link href="https://fonts.googleapis.com/css2?family=Lato:wght@400;700&family=Satisfy&display=swap" rel="stylesheet">
<style>
  :root {
    --navy: #1c3557;
    --ink: #2a2a2a;
    --paper: #ffffff;
    --backdrop: #d6d6d6;
  }
  * { margin: 0; padding: 0; box-sizing: border-box; }
  html, body {
    width: 1200px; height: 1200px; overflow: hidden;
    background: var(--backdrop);
    font-family: "Lato", Arial, sans-serif;
    color: var(--ink);
  }
  .letterhead {
    position: absolute; left: 211px; top: 35px;
    width: 778px; height: 1130px;
    background: var(--paper);
    box-shadow: 0 4px 18px rgba(0,0,0,0.25);
  }
  .brand {
    position: absolute; left: 40px; top: 39px; width: 260px;
    display: flex; flex-direction: column; align-items: center;
  }
  .brand-dot {
    width: 116px; height: 116px; border-radius: 50%;
    background: var(--navy);
  }
  .brand-name {
    margin-top: 16px;
    font-weight: 700; color: var(--navy);
    font-size: 19px; line-height: 22px; letter-spacing: 0.5px;
    text-transform: uppercase; text-align: center;
  }
  .brand-name .sub { display: block; font-size: 12px; line-height: 16px; letter-spacing: 4px; }
  .contact {
    position: absolute; left: 535px; top: 41px; height: 147px;
    border-left: 2px solid var(--navy);
    padding-left: 13px;
    font-style: normal;
    font-size: 12.5px; line-height: 17px; color: #1a1a1a;
  }
  .contact .hours { margin-top: 1px; margin-bottom: 5px; }
  .contact .address { margin-bottom: 5px; }
  .contact-row { display: flex; align-items: center; gap: 8px; height: 18px; }
  .contact-row svg { width: 10px; height: 10px; fill: var(--navy); flex-shrink: 0; }
  .block { position: absolute; left: 50px; }
  .date { top: 287px; font-size: 16.5px; line-height: 20px; }
  .recipient { font-size: 15.5px; line-height: 18.5px; }
  .recipient.person { top: 326px; }
  .recipient.company { top: 383px; }
  .salutation { top: 463px; font-size: 18px; line-height: 22px; font-weight: 700; }
  .body { top: 506px; width: 691px; font-size: 14.8px; line-height: 18.4px; }
  .body p { text-align: justify; margin-bottom: 16px; }
  .closing { top: 827px; font-size: 14.5px; line-height: 18px; }
  .signature {
    top: 872px;
    font-family: "Satisfy", cursive;
    font-size: 34px; line-height: 44px; color: #111;
  }
</style>
</head>
<body>
  <main class="letterhead">
    <header>
      <div class="brand">
        <div class="brand-dot"></div>
        <div class="brand-name">Ridgeview Veterinary<span class="sub">Surgery</span></div>
      </div>
      <address class="contact">
        <div class="hours">our opening hours<br>7am to 6pm Monday to<br>Friday and 9am to 1pm Saturday</div>
        <div class="address">48 Tulloch Road,<br>&nbsp;Ashcombe,Tablelands, 4890</div>
        <div class="contact-row">
          <svg viewBox="0 0 24 24"><path d="M6.6 10.8a15.1 15.1 0 0 0 6.6 6.6l2.2-2.2a1 1 0 0 1 1-.25 11.4 11.4 0 0 0 3.6.57 1 1 0 0 1 1 1V20a1 1 0 0 1-1 1A17 17 0 0 1 3 4a1 1 0 0 1 1-1h3.5a1 1 0 0 1 1 1c0 1.25.2 2.45.57 3.57a1 1 0 0 1-.25 1z"/></svg>
          <span>07 4158 6734</span>
        </div>
        <div class="contact-row">
          <svg viewBox="0 0 24 24"><path d="M2 5h20v14H2z"/></svg>
          <span>admin@ridgeviewvets.com.au</span>
        </div>
        <div class="contact-row">
          <svg viewBox="0 0 24 24"><circle cx="12" cy="12" r="10"/></svg>
          <span>www.ridgeviewvets.com.au</span>
        </div>
      </address>
    </header>

    <p class="block date">January-03-2020</p>
    <p class="block recipient person">Mr, Daniel Hart<br>President</p>
    <p class="block recipient company">Crestline Holdings<br>56 Harbour Lane, Suite# 10<br>City, State, 120023</p>
    <p class="block salutation">Dear Mr, Daniel</p>
    <div class="block body">
      <p>Lorem ipsum dolor sit amet, consectetur adipisicing elit, sed do eiusmod tempor incididunt ut labore et dolore magna aliqua. Ut enim ad minim veniam, quis nostrud exercitation ullamco laboris nisi ut aliquip ex ea commodo consequat. Duis aute irure dolor in reprehenderit in voluptate velit esse cillum dolore eu fugiat nulla pariatur.</p>
      <p>Lorem ipsum dolor sit amet, consectetur adipisicing elit, sed do eiusmod tempor incididunt ut labore et dolore magna aliqua. Ut enim ad minim veniam, quis nostrud exercitation ullamco laboris nisi ut aliquip ex ea commodo consequat. Duis aute irure dolor in reprehenderit in voluptate velit esse cillum dolore eu fugiat nulla pariatur.</p>
      <p>Lorem ipsum dolor sit amet, consectetur adipisicing elit, sed do eiusmod tempor incididunt ut labore et dolore magna aliqua. Ut enim ad minim veniam, quis nostrud exercitation ullamco laboris nisi ut aliquip ex ea commodo consequat.</p>
      <p>Excepteur sint occaecat cupidatat non proident, sunt in culpa qui officia deserunt mollit anim id est laborum. re et dolore magnam aliquam quaerat voluptatem.</p>
    </div>
    <p class="block closing">Regards</p>
    <p class="block signature">Peter Lawson</p>
  </main>
</body>
</html>
```